Velorine Jewellery Display Card

We are a jewellery manufacturer and need artwork for an A4 size strut card to advertise our new "Crescent Loop Pendant "
In the attached files is a picture of the new pendant and artwork for our trademark "Velorine"
We also need to include the phrase " an expression of love "
as part of the artwork.
The background colour should be predominately white

Target Market(s)

This product has been designed as a gift for Mothers as it has their children names
engraved on the pendant

Industry/Entity Type

Manufacturer

Font styles to use
Serif
Script

Colors
ffffff

Requirements
Must have
• Artwork should be simple and elegant , the predominant look in Australian jewellery stores which is where these display cards will be is white, bright and elegant

```html
<!DOCTYPE html>
<html lang="en">
<head>
<meta charset="utf-8">
<title>Velorine – Crescent Loop Pendant Display Card</title>
<link rel="stylesheet" href="https://fonts.googleapis.com/css2?family=Cormorant+Garamond:ital,wght@0,500;0,600;1,600&family=Great+Vibes&display=swap">
<style>
  :root {
    --silver-light: #ffffff;
    --silver-mid: #e9e9ea;
    --silver-deep: #c9c9cc;
    --brand-grey: #8d8d90;
    --band-black: #0b0b0b;
    --band-text: #ffffff;
    --ink: #111111;
    --rule: #1a1a1a;
  }
  * { margin: 0; padding: 0; box-sizing: border-box; }
  html, body { width: 900px; height: 1200px; overflow: hidden; background: var(--silver-mid); }
  .display-card {
    position: relative;
    width: 900px;
    height: 1200px;
    overflow: hidden;
    background:
      radial-gradient(ellipse 70% 45% at 50% 32%, var(--silver-light) 0%, rgba(255,255,255,0) 70%),
      linear-gradient(160deg, var(--silver-light) 0%, var(--silver-mid) 38%, var(--silver-deep) 62%, var(--silver-mid) 80%, var(--silver-light) 100%);
  }
  .brand-name {
    position: absolute;
    top: 92px;
    left: 0;
    width: 100%;
    text-align: center;
    font-family: "Cormorant Garamond", serif;
    font-weight: 500;
    font-size: 70px;
    letter-spacing: 4px;
    color: var(--brand-grey);
    text-transform: uppercase;
  }
  .product-photo {
    position: absolute;
    top: 200px;
    left: 255px;
    width: 390px;
    height: 470px;
    border-radius: 48% 48% 46% 46% / 40% 40% 58% 58%;
    background: radial-gradient(ellipse at 45% 45%, #fafafa 0%, #d7d7d9 45%, #a9a9ad 75%, rgba(200,200,204,0) 100%);
  }
  .product-reflection {
    position: absolute;
    top: 680px;
    left: 300px;
    width: 300px;
    height: 80px;
    border-radius: 50%;
    background: radial-gradient(ellipse at 50% 30%, rgba(190,190,194,0.55) 0%, rgba(255,255,255,0) 70%);
  }
  .product-band {
    position: absolute;
    top: 782px;
    left: 0;
    width: 100%;
    height: 92px;
    background: var(--band-black);
    display: flex;
    align-items: center;
    justify-content: center;
  }
  .product-band::before,
  .product-band::after {
    content: "";
    position: absolute;
    left: 0;
    width: 100%;
    height: 2px;
    background: rgba(255,255,255,0.75);
  }
  .product-band::before { top: 8px; }
  .product-band::after { bottom: 8px; }
  .product-name {
    font-family: "Cormorant Garamond", serif;
    font-weight: 600;
    font-size: 48px;
    letter-spacing: 2px;
    color: var(--band-text);
    text-transform: uppercase;
  }
  .tagline {
    position: absolute;
    top: 935px;
    left: 0;
    width: 100%;
    text-align: center;
  }
  .tagline-intro {
    display: flex;
    align-items: center;
    justify-content: center;
    gap: 26px;
    font-family: "Great Vibes", cursive;
    font-size: 52px;
    color: var(--ink);
  }
  .tagline-intro .rule {
    width: 170px;
    height: 2px;
    background: var(--rule);
  }
  .tagline-main {
    margin-top: 4px;
    font-family: "Cormorant Garamond", serif;
    font-style: italic;
    font-weight: 600;
    font-size: 104px;
    line-height: 1;
    letter-spacing: 3px;
    color: var(--ink);
    text-transform: uppercase;
  }
</style>
</head>
<body>
  <main class="display-card">
    <div class="brand-name">Velorine</div>

    <div class="product-photo" role="img" aria-label="Photograph of the silver Crescent Loop Pendant with tree-of-life centre and engraved children's names"></div>
    <div class="product-reflection"></div>

    <div class="product-band">
      <h1 class="product-name">Crescent Loop Pendant</h1>
    </div>

    <div class="tagline">
      <div class="tagline-intro"><span class="rule"></span>an expression<span class="rule"></span></div>
      <div class="tagline-main">of Love</div>
    </div>
  </main>
</body>
</html>
```